Talvor GmbH business card

We Talvor GmbH based in Switzerland are looking for a business card design. The Fresh Jung, appealing to customers of all kinds. We already have a logo to upload but still a business card. Details: Talvor GmbH Address: Lindenweg 14b in 9476 Brugwil. Tel: 41 79 462 37 18, web: Talvor.ch, E-mail: info@Talvor.ch Facebook: Talvor GmbH. I am the Managing Director: Luka Petrovac. On reverse: Title: Transporter and bus rental Gross: Without deposit Super prices
Contact Information for Business Card
Siehe Projektbeschreibung
Requirements
Should not have
- Other pictures

```html
<!DOCTYPE html>
<html lang="de">
<head>
<meta charset="utf-8">
<title>Talvor GmbH – Visitenkarte</title>
<link rel="stylesheet" href="https://fonts.googleapis.com/css2?family=Roboto:wght@400;500;700&display=swap">
<style>
  :root {
    --page: #e8e8e8;
    --navy: #1e1f63;
    --steel: #4c6c9e;
    --accent-text: #7d95b8;
    --paper: #f3f3f3;
    --ink: #3a3a3a;
    --icon: #6b6f7a;
    --white: #ffffff;
    --muted-white: #dfe2ee;
  }
  html, body {
    margin: 0;
    width: 1200px;
    height: 576px;
    overflow: hidden;
    background: var(--page);
    font-family: "Roboto", Arial, sans-serif;
  }
  .stage { position: relative; width: 1200px; height: 576px; }
  .card {
    position: absolute;
    top: 138px;
    width: 484px;
    height: 294px;
    border-radius: 6px;
    overflow: hidden;
  }
  .card--front { left: 82px; background: var(--paper); }
  .card--back { left: 602px; height: 291px; width: 480px; background: var(--navy); }

  .front-shape { position: absolute; inset: 0; }

  .brand {
    position: absolute; left: 20px; top: 30px;
    display: flex; align-items: center; gap: 10px;
  }
  .brand-square { width: 26px; height: 26px; background: var(--navy); }
  .brand-name {
    font-size: 29px; font-weight: 700; color: var(--navy);
    letter-spacing: 1px; line-height: 1;
  }

  .address {
    position: absolute; left: 20px; top: 171px;
    margin: 0; font-size: 13px; color: var(--ink);
  }
  .contact-list {
    position: absolute; left: 20px; top: 198px;
    margin: 0; padding: 0; list-style: none;
    font-size: 13px; color: var(--ink);
  }
  .contact-list li { display: flex; align-items: center; height: 17.5px; }
  .contact-icon { width: 11px; height: 11px; margin: 0 11px 0 0; fill: var(--icon); flex: none; }

  .person {
    position: absolute; right: 26px; top: 228px; text-align: right; color: var(--white);
  }
  .person-name { margin: 0; font-size: 17.5px; font-weight: 500; }
  .person-role { margin: 5px 0 0; font-size: 10.5px; color: var(--muted-white); }

  .offer {
    position: absolute; left: 0; right: 0; top: 102px;
    text-align: center; color: var(--white);
  }
  .offer-title { margin: 0; font-size: 16px; font-weight: 400; }
  .offer-highlight {
    margin: 8px 0 0; font-size: 24px; font-weight: 700;
    color: var(--accent-text); letter-spacing: 0.5px;
  }
  .offer-sub { margin: 6px 0 0; font-size: 15px; }
</style>
</head>
<body>
<main class="stage">
  <section class="card card--front" aria-label="Vorderseite">
    <svg class="front-shape" width="484" height="294" viewBox="0 0 484 294" aria-hidden="true">
      <polygon points="278,0 296,0 234,294 230,294" fill="var(--steel)"/>
      <polygon points="294,0 484,0 484,294 230,294" fill="var(--navy)"/>
    </svg>

    <div class="brand">
      <span class="brand-square" aria-hidden="true"></span>
      <span class="brand-name">Talvor</span>
    </div>

    <p class="address">Lindenweg 14b in 9476 Brugwil</p>
    <ul class="contact-list">
      <li>
        <svg class="contact-icon" viewBox="0 0 12 12" aria-hidden="true"><path d="M1 3.5C1 2 2.5 1 6 1s5 1 5 2.5V5H8.5V3.8h-5V5H1z M2.5 6h7l1 5h-9z"/></svg>
        +41 79 462 37 18
      </li>
      <li>
        <svg class="contact-icon" viewBox="0 0 12 12" aria-hidden="true"><path d="M6 .5a5.5 5.5 0 1 0 0 11 5.5 5.5 0 0 0 0-11zm0 1c.8.8 1.3 2 1.5 3.5h-3C4.7 3.5 5.2 2.3 6 1.5zM1.6 5h1.9c.1-1.3.4-2.4 1-3.2A4.5 4.5 0 0 0 1.6 5zm6.9 0h1.9a4.5 4.5 0 0 0-2.9-3.2c.6.8.9 1.9 1 3.2zM1.6 7a4.5 4.5 0 0 0 2.9 3.2c-.6-.8-.9-1.9-1-3.2zm2.9 0c.2 1.5.7 2.7 1.5 3.5.8-.8 1.3-2 1.5-3.5zm4 0c-.1 1.3-.4 2.4-1 3.2A4.5 4.5 0 0 0 10.4 7z"/></svg>
        www.Talvor.ch
      </li>
      <li>
        <svg class="contact-icon" viewBox="0 0 12 12" aria-hidden="true"><path d="M0.5 2.5h11v7h-11z M1 3l5 4 5-4" fill="var(--icon)" stroke="var(--paper)" stroke-width="0.8"/></svg>
        info@Talvor.ch
      </li>
      <li>
        <svg class="contact-icon" viewBox="0 0 12 12" aria-hidden="true"><rect x="1" y="1" width="10" height="10"/></svg>
        Talvor GmbH
      </li>
    </ul>

    <div class="person">
      <p class="person-name">Luka Petrovac</p>
      <p class="person-role">Geschäftsführer</p>
    </div>
  </section>

  <section class="card card--back" aria-label="Rückseite">
    <div class="offer">
      <p class="offer-title">Transporter und Bus Vermietung</p>
      <p class="offer-highlight">OHNE KAUTION</p>
      <p class="offer-sub">Super Preise</p>
    </div>
  </section>
</main>
</body>
</html>
```